Use your magic to make a startup company look established*

We are in need of a website that gives the appearance that we are established rather than new. Our audience is comprised of senior executives in technology professional services companies, financial people (conservative) that invest in them, and executives in companies that are in need of their services. The site therefore needs to lean towards the conservative side while being modern and professional.

This should be a fairly simple site.

- About us
- Services
- Contacts
- Content (Articles)

It should be SEO friendly and easy to add content or sub pages. A responsive design is mandatory.

Target Market(s)

We work with executives and investors in professional services companies to more effectively compete in the already crowded “digital transformation” market.

Industry/Entity Type

Professional Service

Coding

Coded - Design and coding required

Number of Pages Required

5+ page

Font styles to use
Sans Serif

Requirements
Must have
• - Responsive design
- Easy to add/change content
- Easy to add additional pages

```html
<!DOCTYPE html>
<html lang="en">
<head>
<meta charset="utf-8">
<title>Summit Crest Partners</title>
<link rel="stylesheet" href="https://fonts.googleapis.com/css2?family=Montserrat:wght@600;700&family=IBM+Plex+Sans:wght@400;500;600&display=swap">
<style>
:root{
  --gold-1:#ebc94f;
  --gold-2:#c39a35;
  --gold-text:#d6ae3c;
  --ink:#141414;
  --body:#3f3f3f;
  --muted:#555;
  --cream:#f8f3e8;
  --footer:#050505;
  --white:#fff;
}
*{box-sizing:border-box;margin:0;padding:0}
html,body{width:1200px;height:2774px;overflow:hidden}
body{position:relative;background:var(--white);font-family:"IBM Plex Sans",Arial,sans-serif;color:var(--body)}
.abs{position:absolute}
.gold-bg{background:linear-gradient(100deg,var(--gold-1),var(--gold-2))}
.h-font{font-family:"Montserrat",Arial,sans-serif}
.btn{position:absolute;display:flex;align-items:center;justify-content:center;color:var(--white);font-weight:600;font-size:16px;border-radius:3px;background:linear-gradient(100deg,var(--gold-1),var(--gold-2))}

/* top bar */
.topbar{left:0;top:0;width:1200px;height:47px;color:var(--white);font-size:16px}
.topbar .contact{position:absolute;left:115px;top:14px;display:flex;gap:20px;align-items:center}
.topbar .contact span{display:flex;align-items:center;gap:6px}
.topbar .follow{position:absolute;right:110px;top:14px;display:flex;align-items:center;gap:14px;font-size:15px}
.dot{width:12px;height:12px;border-radius:50%;background:rgba(255,255,255,.9)}

/* header */
.header{left:0;top:47px;width:1200px;height:101px;background:var(--white)}
.brand{position:absolute;display:flex;align-items:center;gap:10px;font-family:"Montserrat",Arial,sans-serif;font-weight:600;color:var(--gold-2)}
.brand .sq{width:34px;height:34px;border:3px solid var(--gold-2)}
.brand .name{font-size:13px;letter-spacing:1.5px;line-height:1.3;text-transform:uppercase}
.nav{position:absolute;top:42px;left:405px;display:flex;gap:0;font-family:"Montserrat",Arial,sans-serif;font-weight:700;font-size:16px;color:var(--ink);letter-spacing:.5px}
.nav a{position:absolute;white-space:nowrap;text-decoration:none;color:inherit}

/* hero */
.hero{left:0;top:148px;width:1200px;height:598px;background:linear-gradient(110deg,#6f5a45 0%,#b49b83 30%,#d8ccc1 60%,#8b7c70 100%)}
.hero-panel{left:111px;top:242px;width:451px;height:312px;background:rgba(70,70,70,.72)}
.hero-title{left:151px;top:276px;width:420px;font-size:45px;line-height:52px;color:var(--white);font-weight:700}
.hero-text{left:151px;top:390px;width:380px;font-size:16px;line-height:24px;color:var(--white)}

/* feature cards */
.feature{position:absolute;background:var(--white);box-shadow:0 3px 14px rgba(0,0,0,.12);text-align:center;padding:0 24px}
.feature.active{background:linear-gradient(160deg,var(--gold-1),var(--gold-2));color:var(--white)}
.icon-ph{margin:0 auto;border-radius:50%;background:radial-gradient(circle,#f0d57a,#cfa640)}
.active .icon-ph{background:radial-gradient(circle,#fff6d8,#f3dc95)}
.feature h3{font-family:"Montserrat",Arial,sans-serif;font-size:20px;font-weight:700;color:var(--ink);margin-top:22px}
.feature.active h3{color:var(--white)}
.feature p{font-size:16px;line-height:24px;margin-top:12px;color:var(--body)}
.feature.active p{color:#fdf6e0}
.more{display:inline-flex;align-items:center;gap:8px;margin-top:12px;font-size:16px;font-weight:600;color:var(--gold-text)}
.active .more{color:var(--white)}

/* about */
.about-band{left:0;top:1212px;width:1200px;height:441px;background:var(--cream)}
.about-img{left:101px;top:1160px;width:479px;height:329px;background:linear-gradient(120deg,#7e8a93,#d9d6d1 55%,#9a948c)}
.play{position:absolute;left:315px;top:1300px;width:50px;height:50px;border-radius:50%;background:var(--white);display:flex;align-items:center;justify-content:center}
.eyebrow{font-family:"Montserrat",Arial,sans-serif;font-weight:600;font-size:19px;color:var(--gold-text)}
.about-h{left:636px;top:1317px;font-size:34px;line-height:41px;color:var(--ink);font-weight:700;width:520px}
.about-p{left:636px;top:1410px;width:460px;font-size:16px;line-height:24px}

/* services */
.svc-h{left:136px;top:1806px;font-size:35px;font-weight:700;color:var(--ink)}
.svc-p{left:137px;top:1864px;width:270px;font-size:16px;line-height:24px}
.svc{position:absolute;width:288px;height:263px;background:var(--white);box-shadow:0 3px 14px rgba(0,0,0,.12);text-align:center;border-bottom:5px solid var(--gold-2);padding:40px 20px 0}
.svc .icon-ph{width:52px;height:52px}
.svc h3{font-family:"Montserrat",Arial,sans-serif;font-size:19px;font-weight:700;color:var(--ink);margin-top:26px}
.svc p{font-size:16px;line-height:24px;margin-top:14px}

/* footer */
.footer{left:0;top:2417px;width:1200px;height:357px;background:var(--footer);color:var(--white)}
.footer h4{position:absolute;top:75px;font-family:"IBM Plex Sans",Arial,sans-serif;font-weight:600;font-size:17px}
.footer ul{position:absolute;list-style:none;font-size:16px;line-height:30px}
.footer .about{position:absolute;left:118px;top:138px;width:240px;font-size:16px;line-height:24px}
.social{position:absolute;left:924px;top:107px;display:flex;gap:6px}
.social span{width:36px;height:36px;border-radius:50%;background:linear-gradient(140deg,var(--gold-1),var(--gold-2))}
.rule{position:absolute;left:112px;top:258px;width:976px;height:1px;background:#2a2a2a}
.copy{position:absolute;left:0;top:296px;width:1200px;text-align:center;font-size:16px}
</style>
</head>
<body>

<div class="abs topbar gold-bg">
  <div class="contact">
    <span><svg width="14" height="14" viewBox="0 0 24 24" fill="#fff"><path d="M6.6 10.8a15 15 0 0 0 6.6 6.6l2.2-2.2c.3-.3.7-.4 1-.2 1.1.4 2.3.6 3.6.6.6 0 1 .4 1 1V20c0 .6-.4 1-1 1A17 17 0 0 1 3 4c0-.6.4-1 1-1h3.5c.6 0 1 .4 1 1 0 1.3.2 2.5.6 3.6.1.3 0 .7-.2 1z"/></svg>100-555-0142</span>
    <span><svg width="17" height="13" viewBox="0 0 24 18" fill="none" stroke="#fff" stroke-width="2"><rect x="1" y="1" width="22" height="16"/><path d="M1 1l11 9 11-9"/></svg>contact@summitcrestpartners.com</span>
  </div>
  <div class="follow">Follow us :<span class="dot"></span><span class="dot"></span><span class="dot"></span><span class="dot"></span></div>
</div>

<header class="abs header">
  <div class="brand" style="left:113px;top:30px"><span class="sq"></span><span class="name">Summit Crest<br>Partners</span></div>
  <nav class="nav">
    <a style="left:0">HOME</a>
    <a style="left:100px">ABOUT US</a>
    <a style="left:235px">SERVICES</a>
    <a style="left:365px">CONTACT US</a>
  </nav>
  <a class="btn" style="left:931px;top:26px;width:157px;height:51px;letter-spacing:.5px">GET STARTED</a>
</header>

<section>
  <div class="abs hero" role="img" aria-label="Photo of two businesswomen reviewing documents at an office desk"></div>
  <div class="abs hero-panel"></div>
  <h1 class="abs hero-title h-font">Summit Crest Partners</h1>
  <p class="abs hero-text">Sed ut perspiciatis unde omnis iste natus error sit voluptatem accusantium doloremque laudantium,</p>
  <a class="btn" style="left:148px;top:461px;width:146px;height:50px">CONTACT US</a>

  <div class="feature" style="left:112px;top:683px;width:294px;height:335px">
    <div class="icon-ph" style="width:100px;height:100px;margin-top:38px" role="img" aria-label="Lightbulb with gear icon"></div>
    <h3>Innovative Solutions</h3>
    <p>Sed ut perspiciatis unde omnis iste natus error sit voluptatem accusantium doloremque</p>
    <span class="more">READ MORE <svg width="16" height="10" viewBox="0 0 16 10" fill="none" stroke="currentColor" stroke-width="1.5"><path d="M0 5h15M11 1l4 4-4 4"/></svg></span>
  </div>
  <div class="feature active" style="left:453px;top:651px;width:295px;height:400px">
    <div class="icon-ph" style="width:110px;height:90px;margin-top:55px;border-radius:45px" role="img" aria-label="Team of people icon"></div>
    <h3>Professional Team</h3>
    <p>Sed ut perspiciatis unde omnis iste natus error sit voluptatem accusantium doloremque totam rem aperiam, eaque ipsa quae ab illo inventore veritatis et</p>
    <span class="more">READ MORE <svg width="16" height="10" viewBox="0 0 16 10" fill="none" stroke="currentColor" stroke-width="1.5"><path d="M0 5h15M11 1l4 4-4 4"/></svg></span>
  </div>
  <div class="feature" style="left:794px;top:683px;width:294px;height:335px">
    <div class="icon-ph" style="width:100px;height:100px;margin-top:38px" role="img" aria-label="Support desk with computer icon"></div>
    <h3>24/7 Support</h3>
    <p>Sed ut perspiciatis unde omnis iste natus error sit voluptatem accusantium doloremque</p>
    <span class="more">READ MORE <svg width="16" height="10" viewBox="0 0 16 10" fill="none" stroke="currentColor" stroke-width="1.5"><path d="M0 5h15M11 1l4 4-4 4"/></svg></span>
  </div>
</section>

<section>
  <div class="abs about-band"></div>
  <div class="abs about-img" role="img" aria-label="Photo of business people shaking hands at a meeting table"></div>
  <div class="play"><svg width="16" height="18" viewBox="0 0 16 18"><path d="M0 0l16 9-16 9z" fill="#d6ae3c"/></svg></div>
  <div class="abs eyebrow" style="left:636px;top:1288px">About Us</div>
  <h2 class="abs about-h h-font">Summit Crest Partners is a professional</h2>
  <p class="abs about-p">Firm that advises professional services companies on how to increase revenue and margins, and systematically acquire new clients.Our clients can expect to become strategic partners with their clients rather than just vendors.</p>
  <a class="btn" style="left:629px;top:1527px;width:136px;height:46px">LEARN MORE</a>
</section>

<section>
  <div class="abs eyebrow" style="left:135px;top:1777px">Our Services</div>
  <h2 class="abs svc-h h-font">Lorem ipsum</h2>
  <p class="abs svc-p">Sed ut perspiciatis unde omnis iste natus error sit voluptate accusantium doloremque laudantium, totam rem</p>
  <a class="btn" style="left:139px;top:1941px;width:132px;height:46px">VIEW ALL</a>

  <div class="svc" style="left:460px;top:1762px"><div class="icon-ph" role="img" aria-label="Hand holding coin icon"></div><h3>Manage Investment</h3><p>Sed ut perspiciatis unde omnis iste natus error sit voluptatem accusantium doloremque</p></div>
  <div class="svc" style="left:776px;top:1762px"><div class="icon-ph" role="img" aria-label="Report document icon"></div><h3>Financial Report</h3><p>Sed ut perspiciatis unde omnis iste natus error sit voluptatem accusantium doloremque</p></div>
  <div class="svc" style="left:139px;top:2057px"><div class="icon-ph" role="img" aria-label="Chart with currency coin icon"></div><h3>Audit &amp; Assurance</h3><p>Sed ut perspiciatis unde omnis iste natus error sit voluptatem accusantium doloremque</p></div>
  <div class="svc" style="left:458px;top:2057px"><div class="icon-ph" role="img" aria-label="Stack of coins icon"></div><h3>Financial Plan</h3><p>Sed ut perspiciatis unde omnis iste natus error sit voluptatem accusantium doloremque</p></div>
  <div class="svc" style="left:776px;top:2057px"><div class="icon-ph" role="img" aria-label="Hand with rising chart icon"></div><h3>Profit Planning</h3><p>Sed ut perspiciatis unde omnis iste natus error sit voluptatem accusantium doloremque</p></div>
</section>

<footer class="abs footer">
  <div class="brand" style="left:120px;top:62px"><span class="sq"></span><span class="name">Summit Crest<br>Partners</span></div>
  <p class="about">Sed ut perspiciatis unde omnis iste natus error sit voluptatem accusantium doloremque laudantium, totam rem aperiam,</p>
  <h4 style="left:441px">QUICK LINK</h4>
  <ul style="left:444px;top:105px"><li>Home</li><li>About us</li><li>Services</li><li>Contact us</li></ul>
  <h4 style="left:636px">CONTACT US</h4>
  <ul style="left:636px;top:105px">
    <li style="display:flex;gap:8px"><svg width="11" height="15" viewBox="0 0 12 16" style="margin-top:7px" fill="#fff"><path d="M6 0a6 6 0 0 0-6 6c0 4.5 6 10 6 10s6-5.5 6-10a6 6 0 0 0-6-6zm0 8.5A2.5 2.5 0 1 1 6 3.5a2.5 2.5 0 0 1 0 5z"/></svg><span>No 105 Lorem ipsum<br>dolor sit amet</span></li>
    <li style="display:flex;gap:6px;margin-top:4px;align-items:center"><svg width="13" height="13" viewBox="0 0 24 24" fill="#fff"><path d="M6.6 10.8a15 15 0 0 0 6.6 6.6l2.2-2.2c.3-.3.7-.4 1-.2 1.1.4 2.3.6 3.6.6.6 0 1 .4 1 1V20c0 .6-.4 1-1 1A17 17 0 0 1 3 4c0-.6.4-1 1-1h3.5c.6 0 1 .4 1 1 0 1.3.2 2.5.6 3.6.1.3 0 .7-.2 1z"/></svg>100-555-0142</li>
    <li style="display:flex;gap:6px;margin-top:4px;align-items:center"><svg width="15" height="11" viewBox="0 0 24 18" fill="none" stroke="#fff" stroke-width="2"><rect x="1" y="1" width="22" height="16"/><path d="M1 1l11 9 11-9"/></svg>hello@summitcrestpartners.com</li>
  </ul>
  <h4 style="left:924px">FOLLOW US</h4>
  <div class="social"><span></span><span></span><span></span><span></span></div>
  <div class="rule"></div>
  <p class="copy">COPYRIGHTS 2021 SUMMIT CREST &nbsp;|&nbsp; ALL RIGHTS RESERVED</p>
</footer>

</body>
</html>
```